Web Design for Financial Consulting Company

We need a website design for a financial consulting company "Korvane Consulting". We build financial models, scenario analysis, handle the budgeting process and provide temporary staffing. I have over 10 years of experience. My Excel expertise and analytical savvy has saved clients over $17 million in profit.

Target Market(s)

Small to medium businesses

Industry/Entity Type

Financial Consulting

Number of Pages Required

4 page

Requirements
Must have
• Professional looking
Nice to have
• A little futuristic looking

```html
<!DOCTYPE html>
<html lang="en">
<head>
<meta charset="utf-8">
<title>Korvane Consulting</title>
<link href="https://fonts.googleapis.com/css2?family=Montserrat:wght@500;600;700;800&family=Figtree:wght@400;500;600&display=swap" rel="stylesheet">
<style>
:root{
  --navy:#0a2b57;
  --blue:#0aa2ea;
  --blue-dark:#1a8fd6;
  --bg:#f3f9fd;
  --ink:#1d2b3a;
  --line:#d9e6f0;
  --faint:#dceffa;
}
*{margin:0;padding:0;box-sizing:border-box}
html,body{width:1200px;height:2881px;overflow:hidden}
body{background:var(--bg);font-family:"Figtree",sans-serif;color:var(--ink);position:relative}
.abs{position:absolute}
.brand{display:flex;align-items:center;gap:10px;font-family:"Montserrat",sans-serif;font-weight:800;color:var(--navy);font-size:26px;letter-spacing:1px}
.brand-mark{width:34px;height:34px;border:4px solid var(--blue)}
.nav{top:42px;font-family:"Montserrat",sans-serif;font-weight:700;font-size:14px;color:var(--navy)}
.nav a{position:absolute;color:var(--navy);text-decoration:none;white-space:nowrap}
.nav a.active{color:var(--blue);text-decoration:underline}
.btn-solid{background:var(--blue);color:#fff;font-family:"Montserrat",sans-serif;font-weight:700;display:flex;align-items:center;justify-content:center}
.btn-outline{border:2px solid var(--blue);color:var(--blue);font-size:15px;display:flex;align-items:center;justify-content:center;letter-spacing:.3px}
.eyebrow{color:var(--blue);font-size:17px;letter-spacing:.3px}
.hero-title{font-family:"Montserrat",sans-serif;font-weight:800;color:var(--navy);line-height:1}
.hero-sub{font-family:"Montserrat",sans-serif;font-weight:600;color:var(--blue-dark);font-size:20px;line-height:25px}
.section-title{font-family:"Montserrat",sans-serif;font-weight:800;color:var(--navy);font-size:35px;display:flex;align-items:flex-end;gap:6px;padding-bottom:4px;border-bottom:2px solid var(--blue)}
.about-text{font-size:15px;line-height:21px;color:#222}
.stat-num{font-family:"Montserrat",sans-serif;font-weight:700;color:var(--blue-dark);font-size:25px;line-height:1}
.stat-label{font-size:15px;color:#222}
.service{position:absolute;width:320px;text-align:center}
.service-icon{width:100px;height:100px;margin:0 auto;background:#fff;box-shadow:0 2px 10px rgba(10,43,87,.12);display:flex;align-items:center;justify-content:center}
.service-icon.selected{border:3px solid var(--blue)}
.service h3{font-family:"Figtree",sans-serif;font-weight:600;font-size:18px;color:var(--navy);margin-top:27px}
.service.selected h3{color:var(--blue)}
.service p{font-size:15px;line-height:20px;color:#222;margin:6px auto 0}
.field-label{font-size:13px;color:#444;letter-spacing:.4px}
.field{background:#fff;border:1px solid var(--line)}
.cta{background:var(--navy)}
.foot-h{font-family:"Figtree",sans-serif;font-weight:600;font-size:19px;color:var(--blue)}
.foot-list{font-size:15px;color:#111;line-height:24.5px;list-style:none}
.foot-list a{color:#111;text-decoration:none}
.foot-list a.active{color:var(--blue);text-decoration:underline}
.bottom-bar{background:var(--blue)}
.social{width:24px;height:24px;border:1px solid #fff}
.social.on{background:#fff}
</style>
</head>
<body>

<svg class="abs" style="left:0;top:0" width="1200" height="2881" aria-hidden="true">
  <g fill="none" stroke="var(--faint)" stroke-width="12">
    <rect x="-20" y="560" width="120" height="160" transform="rotate(-20 40 640)"/>
    <rect x="1040" y="1650" width="160" height="200" transform="rotate(20 1120 1750)"/>
    <rect x="1120" y="2660" width="120" height="140" transform="rotate(40 1180 2730)"/>
  </g>
  <rect x="930" y="1100" width="70" height="70" fill="none" stroke="var(--faint)" stroke-width="6" transform="rotate(-35 965 1135)"/>
</svg>

<div class="abs brand" style="left:88px;top:28px"><span class="brand-mark"></span>Korvane Consulting</div>

<svg class="abs" style="left:0;top:0" width="1200" height="600" role="img" aria-label="Business analyst reviewing bar and line charts on printed reports">
  <defs>
    <linearGradient id="heroA" x1="0" y1="0" x2="1" y2="1">
      <stop offset="0" stop-color="#2a3b52"/><stop offset=".55" stop-color="#8aa7c4"/><stop offset="1" stop-color="#e6eef6"/>
    </linearGradient>
  </defs>
  <polygon points="525,129 693,0 1200,0 1200,336 956,587 757,388" fill="url(#heroA)"/>
</svg>
<svg class="abs" style="left:520px;top:175px" width="420" height="410" role="img" aria-label="Consultant presenting charts to a team in a meeting room">
  <defs>
    <linearGradient id="heroB" x1="0" y1="0" x2="1" y2="1">
      <stop offset="0" stop-color="#eef3f8"/><stop offset=".5" stop-color="#9fb0c2"/><stop offset="1" stop-color="#3d3026"/>
    </linearGradient>
  </defs>
  <polygon points="6,210 212,4 414,210 207,406" fill="url(#heroB)" stroke="#fff" stroke-width="3"/>
</svg>

<nav class="abs nav" style="left:0;width:1200px">
  <a class="active" style="left:539px" href="#">HOME</a>
  <a style="left:618px" href="#">ABOUT US</a>
  <a style="left:729px" href="#">SERVICES</a>
  <a style="left:836px" href="#">CONTACT US</a>
</nav>
<div class="abs btn-solid" style="left:968px;top:32px;width:142px;height:34px;font-size:13px">CONSULT NOW!</div>

<div class="abs eyebrow" style="left:87px;top:207px">BEST CONSULTING COMPANY</div>
<div class="abs hero-title" style="left:88px;top:244px;font-size:41px">WE BOOST YOUR</div>
<div class="abs hero-title" style="left:86px;top:294px;font-size:62px">BUSINESS</div>
<div class="abs hero-sub" style="left:88px;top:364px">We've been lucky to collaborate with<br>a long list of customers</div>
<div class="abs btn-outline" style="left:88px;top:457px;width:148px;height:41px">GET STARTED</div>

<svg class="abs" style="left:132px;top:632px" width="428" height="481" role="img" aria-label="Two smiling businessmen reviewing a document together">
  <defs>
    <linearGradient id="aboutG" x1="0" y1="0" x2="1" y2="1">
      <stop offset="0" stop-color="#3a4250"/><stop offset=".5" stop-color="#b59a86"/><stop offset="1" stop-color="#f2ece6"/>
    </linearGradient>
  </defs>
  <polygon points="0,95 427,0 427,481 0,481" fill="url(#aboutG)"/>
</svg>

<div class="abs section-title" style="left:660px;top:700px">ABOUT US
  <svg width="18" height="18" aria-hidden="true"><g fill="none" stroke="var(--blue)" stroke-width="2"><path d="M3 17V12M8 17V9M13 17V5M17 17V2"/></g></svg>
</div>
<p class="abs about-text" style="left:660px;top:769px;width:385px">I am an experienced Finance professional who develops strategic financial plans, provides insightful analysis, and supports decision-making.</p>
<p class="abs about-text" style="left:660px;top:852px;width:385px">With over 10 years of experience, I have successfully increased profitability for clients by $17M</p>
<div class="abs" style="left:660px;top:918px"><div class="stat-num">10</div><div class="stat-label" style="margin-top:3px">years of experience</div></div>
<div class="abs" style="left:854px;top:918px"><div class="stat-num">$17M</div><div class="stat-label" style="margin-top:3px">clients</div></div>
<div class="abs btn-solid" style="left:660px;top:1003px;width:133px;height:37px;font-family:'Figtree',sans-serif;font-weight:500;font-size:15px">READ MORE</div>

<div class="abs section-title" style="left:499px;top:1209px">SERVICES
  <svg width="18" height="18" aria-hidden="true"><g fill="none" stroke="var(--blue)" stroke-width="2"><path d="M3 17V12M8 17V9M13 17V5M17 17V2"/></g></svg>
</div>

<div class="service" style="left:90px;top:1317px">
  <div class="service-icon"><svg width="54" height="54" fill="none" stroke="var(--navy)" stroke-width="2"><rect x="6" y="6" width="34" height="42"/><path d="M12 42V34M18 42V30M24 42V32M30 42V26M12 16h10M12 22h14"/><circle cx="40" cy="22" r="8"/><path d="M40 17v10M37 20h5"/></svg></div>
  <h3>Financial Models</h3>
  <p>Financial analysis, scenario modeling,<br>pricing analysis, projects</p>
</div>
<div class="service" style="left:445px;top:1317px">
  <div class="service-icon"><svg width="54" height="54" fill="none" stroke="var(--navy)" stroke-width="2"><path d="M10 46V32h6v14M24 46V26h6v14M38 46V22h6v24"/><circle cx="13" cy="24" r="5"/><circle cx="27" cy="16" r="5"/><circle cx="41" cy="11" r="6"/></svg></div>
  <h3>Budgeting Process</h3>
  <p style="width:290px">Building budgets from scratch, revamping current process to be more robust and scalable.</p>
</div>
<div class="service selected" style="left:793px;top:1317px">
  <div class="service-icon selected"><svg width="54" height="54" fill="none" stroke="var(--navy)" stroke-width="2"><circle cx="27" cy="18" r="11"/><circle cx="27" cy="18" r="4"/><path d="M6 46v-6a6 6 0 0 1 12 0v6zM20 46v-8a7 7 0 0 1 14 0v8zM36 46v-6a6 6 0 0 1 12 0v6z"/></svg></div>
  <h3>Temporary Staffing</h3>
  <p style="width:290px">Years of Financial Planning and Analysis experience across multiple industries can help temporary staffing needs.</p>
</div>
<div class="service" style="left:266px;top:1572px">
  <div class="service-icon"><svg width="54" height="54" fill="none" stroke="var(--navy)" stroke-width="2"><ellipse cx="22" cy="10" rx="14" ry="5"/><path d="M8 10v26c0 3 6 5 14 5M36 10v12M8 19c0 3 6 5 14 5s14-2 14-5M8 28c0 3 6 5 14 5"/><path d="M30 46l16-16M40 30l6 6"/></svg></div>
  <h3>Data Cleansing</h3>
  <p>Lorem Ipsum is dummy text of the<br>printing industry.</p>
</div>
<div class="service" style="left:617px;top:1572px">
  <div class="service-icon"><svg width="54" height="54" fill="none" stroke="var(--navy)" stroke-width="2"><path d="M6 38l12-12 8 8 18-18"/><path d="M36 14h9v9"/><circle cx="24" cy="42" r="7"/><path d="M24 32v3M24 49v3M14 42h3M31 42h3"/></svg></div>
  <h3>Process Improvement</h3>
  <p>Month end close, reporting,<br>budgeting</p>
</div>

<svg class="abs" style="left:0;top:1660px" width="500" height="760" role="img" aria-label="Hand pointing at financial charts on printed reports, with a smiling support agent wearing a headset">
  <defs>
    <linearGradient id="contactA" x1="0" y1="0" x2="1" y2="1">
      <stop offset="0" stop-color="#35404f"/><stop offset=".5" stop-color="#b9c7d6"/><stop offset="1" stop-color="#eef3f8"/>
    </linearGradient>
    <linearGradient id="contactB" x1="0" y1="0" x2="0" y2="1">
      <stop offset="0" stop-color="#e9eef4"/><stop offset=".55" stop-color="#c9a88e"/><stop offset="1" stop-color="#1f2a4a"/>
    </linearGradient>
  </defs>
  <polygon points="0,130 134,4 497,366 112,753 0,643" fill="url(#contactA)"/>
  <polygon points="78,548 285,341 486,548 280,749" fill="url(#contactB)" stroke="#fff" stroke-width="3"/>
</svg>

<div class="abs section-title" style="left:686px;top:1857px">GET IN TOUCH!
  <svg width="18" height="18" aria-hidden="true"><g fill="none" stroke="var(--blue)" stroke-width="2"><path d="M3 17V12M8 17V9M13 17V5M17 17V2"/></g></svg>
</div>

<div class="abs field-label" style="left:591px;top:1948px">FIRST NAME</div>
<div class="abs field-label" style="left:853px;top:1948px">LAST NAME</div>
<div class="abs field" style="left:589px;top:1968px;width:245px;height:40px"></div>
<div class="abs field" style="left:851px;top:1968px;width:245px;height:40px"></div>
<div class="abs field-label" style="left:591px;top:2021px">EMAIL</div>
<div class="abs field-label" style="left:853px;top:2021px">PHONE</div>
<div class="abs field" style="left:589px;top:2040px;width:245px;height:40px"></div>
<div class="abs field" style="left:851px;top:2040px;width:245px;height:40px"></div>
<div class="abs field-label" style="left:591px;top:2094px">COMMENT OR MESSAGE</div>
<div class="abs field" style="left:589px;top:2113px;width:507px;height:120px"></div>
<div class="abs btn-outline" style="left:790px;top:2258px;width:105px;height:37px">SUBMIT</div>

<div class="abs cta" style="left:88px;top:2466px;width:1024px;height:108px"></div>
<div class="abs" style="left:131px;top:2502px;font-family:'Figtree',sans-serif;font-weight:600;font-size:31px;color:#fff">Let's Start Something Great!</div>
<div class="abs btn-outline" style="left:932px;top:2502px;width:140px;height:37px">LET'S START</div>

<div class="abs" style="left:150px;top:2655px;width:200px;text-align:center">
  <div style="width:62px;height:62px;border:6px solid var(--blue);margin:0 auto"></div>
  <div style="font-family:'Montserrat',sans-serif;font-weight:800;color:var(--navy);font-size:22px;margin-top:20px;line-height:1.1">Korvane<br>Consulting</div>
</div>

<div class="abs foot-h" style="left:453px;top:2633px">Conatct info</div>
<svg class="abs" style="left:453px;top:2678px" width="14" height="20" aria-hidden="true"><path d="M7 1a6 6 0 0 0-6 6c0 5 6 12 6 12s6-7 6-12a6 6 0 0 0-6-6z" fill="var(--blue)"/><circle cx="7" cy="7" r="2.2" fill="#fff"/></svg>
<div class="abs foot-list" style="left:480px;top:2672px;line-height:20px">412 Harbor Crest ln.,<br>Fenwick, CA90417</div>
<svg class="abs" style="left:453px;top:2734px" width="15" height="15" aria-hidden="true"><path d="M3 1l3 0 2 4-2 2a9 9 0 0 0 4 4l2-2 4 2v3c0 1-1 1-2 1A13 13 0 0 1 1 3c0-1 1-2 2-2z" fill="var(--blue)"/></svg>
<div class="abs foot-list" style="left:480px;top:2729px">(555) 214-7730</div>
<svg class="abs" style="left:453px;top:2769px" width="16" height="12" aria-hidden="true"><rect x="0" y="0" width="16" height="12" fill="var(--blue)"/><path d="M0 0l8 7 8-7" fill="none" stroke="#fff" stroke-width="1.4"/></svg>
<div class="abs foot-list" style="left:480px;top:2763px">hello@korvanemail.com</div>

<div class="abs foot-h" style="left:740px;top:2633px">Quick Link</div>
<ul class="abs foot-list" style="left:740px;top:2670px">
  <li><a class="active" href="#">Home</a></li>
  <li><a href="#">About Us</a></li>
  <li><a href="#">Services</a></li>
  <li><a href="#">Contact Us</a></li>
</ul>

<div class="abs foot-h" style="left:911px;top:2633px">Services</div>
<ul class="abs foot-list" style="left:911px;top:2670px">
  <li>Financial Models</li>
  <li>Budgeting Process</li>
  <li>Temporary Staffing</li>
  <li>Data cleansing</li>
  <li>Process Improvement</li>
</ul>

<div class="abs bottom-bar" style="left:0;top:2844px;width:1200px;height:37px"></div>
<div class="abs" style="left:88px;top:2853px;color:#fff;font-size:15px">© 2023 Korvane Consulting. All Right Reserved</div>
<div class="abs" style="left:985px;top:2851px;display:flex;gap:10px">
  <span class="social"></span><span class="social on"></span><span class="social"></span><span class="social"></span>
</div>

</body>
</html>
```